クリニックで使用する封筒(角2、長3の2サイズ)のデザインをお願いします。

【カラーリング】
・別添のロゴマークに使用してある色(グリーン・ブルーや白を基調とした色

【デザイン】
・さりげなくロゴが印象に残る形で

【用途】
(角2)書類の郵送
(長3)同上

※両サイズともデザインを統一して頂ければと思います。
クリニック名(医療法人社団松浦クリニック、医療法人社団は(医)と表記 して可)、郵便番号・住所(158ー0093、東京都豊島区南青葉台4ー7ー3碧山ビル3F、電話番号(03-6281-4370)、ロゴマーク
水色系、緑系

ロゴと字のバランスが良く仕事上で使いやすそうと感じたため選ばせていただきました。

多くのデザインをお寄せいただきありがとうございました。印象にのこるデザイン、目を引くデザインなど多々ありました。今後機会がありましたらぜひよろしくお願いいたします。

```html
<!DOCTYPE html>
<html lang="ja">
<head>
<meta charset="utf-8">
<title>松浦クリニック 封筒 角2</title>
<link href="https://fonts.googleapis.com/css2?family=M+PLUS+Rounded+1c:wght@500;700&family=Noto+Sans+JP:wght@400;500&display=swap" rel="stylesheet">
<style>
  :root {
    --page-bg: #ffffff;
    --paper: #ffffff;
    --paper-edge: #d6d6d6;
    --flap-line: #e4e4e4;
    --clinic-green: #1f9a5c;
    --band-green: #1e9a5f;
    --wave-light: #8fd0a8;
    --text-white: #ffffff;
    --sub-green: #4aa878;
  }
  html, body {
    margin: 0;
    padding: 0;
    width: 822px;
    height: 1200px;
    overflow: hidden;
    background: var(--page-bg);
  }
  .envelope {
    position: absolute;
    left: 10px;
    top: 10px;
    width: 800px;
    height: 1178px;
    background: var(--paper);
    border: 1px solid var(--paper-edge);
    box-shadow: 2px 3px 6px rgba(0,0,0,0.18);
    overflow: hidden;
  }
  .flap-fold {
    position: absolute;
    left: 0;
    right: 0;
    top: 26px;
    border-top: 1px solid var(--flap-line);
  }
  .clinic-mark {
    position: absolute;
    left: 88px;
    top: 948px;
    color: var(--clinic-green);
    font-family: "M PLUS Rounded 1c", sans-serif;
    font-weight: 700;
  }
  .clinic-mark__corp {
    font-family: "Noto Sans JP", sans-serif;
    font-weight: 500;
    font-size: 12px;
    letter-spacing: 0.1em;
    margin: 0 0 6px 46px;
  }
  .clinic-mark__name {
    display: flex;
    align-items: center;
    gap: 10px;
    font-size: 34px;
    letter-spacing: 0.04em;
    line-height: 1;
  }
  .clinic-mark__dot {
    width: 14px;
    height: 14px;
    border-radius: 50%;
    background: var(--clinic-green);
  }
  .clinic-mark__roman {
    font-family: "Noto Sans JP", sans-serif;
    font-weight: 500;
    font-size: 8px;
    letter-spacing: 0.2em;
    color: var(--sub-green);
    margin: 6px 0 0 46px;
  }
  .footer-band {
    position: absolute;
    left: 0;
    bottom: 0;
    width: 800px;
    height: 130px;
  }
  .footer-band svg {
    display: block;
  }
  .footer-band__info {
    position: absolute;
    left: 80px;
    bottom: 30px;
    display: flex;
    gap: 34px;
    color: var(--text-white);
    font-family: "Noto Sans JP", sans-serif;
    font-size: 12px;
    letter-spacing: 0.04em;
  }
</style>
</head>
<body>
  <div class="envelope">
    <div class="flap-fold"></div>

    <div class="clinic-mark">
      <div class="clinic-mark__corp">医療法人社団</div>
      <div class="clinic-mark__name"><span class="clinic-mark__dot"></span>松浦クリニック</div>
      <div class="clinic-mark__roman">MATSUURA CLINIC</div>
    </div>

    <div class="footer-band">
      <svg width="800" height="130" viewBox="0 0 800 130" aria-hidden="true">
        <path d="M0 46 C 160 22, 300 40, 430 44 C 560 48, 680 26, 800 20 L800 130 L0 130 Z" fill="var(--wave-light)"/>
        <path d="M0 58 C 150 36, 300 52, 440 56 C 580 60, 690 40, 800 34 L800 130 L0 130 Z" fill="var(--band-green)"/>
      </svg>
      <div class="footer-band__info">
        <span>〒158ー0093</span>
        <span>東京都豊島区南青葉台4ー7ー3碧山ビル3F</span>
        <span>TEL03-6281-4370</span>
      </div>
    </div>
  </div>
</body>
</html>
```